Redesign existing website.

I need a holidayhouse webdisain. Please review existing website: www.sorvimaja.ee
I want to keep my logo.
Target Market(s)
Nature and sea enjoying holidaymakers, aged 30 to 70
Requirements
Must have
- 3 languages (English, Russian and Estonian)

```html
<!DOCTYPE html>
<html lang="et">
<head>
<meta charset="utf-8">
<title>Sorvimaja puhkemaja</title>
<link href="https://fonts.googleapis.com/css2?family=Arimo:wght@400;700&display=swap" rel="stylesheet">
<style>
:root{
  --ink:#111;
  --text:#3f4450;
  --muted:#555;
  --rule:#cfcfcf;
  --arrow:#4b4f5c;
  --card-border:#f6d4b8;
  --footer-dark:#0f1812;
  --footer-glow:#2a4431;
  --footer-head:#c9bfa8;
  --footer-text:#c8c8c0;
  --footer-rule:#050805;
}
*{margin:0;padding:0;box-sizing:border-box}
html,body{width:1200px;height:932px;overflow:hidden}
body{font-family:"Arimo",Arial,sans-serif;color:var(--text);background:#fff;position:relative}
.top-fade{position:absolute;left:0;top:0;width:1200px;height:110px;background:linear-gradient(#dcdcdc,#fff)}
.block{position:absolute;width:460px}
.block-head{display:flex;justify-content:space-between;align-items:center;gap:10px;height:37px;border-bottom:1px solid var(--rule);white-space:nowrap}
.block-title{font-size:19px;font-weight:700;color:var(--ink);letter-spacing:-.3px;white-space:nowrap}
.more-link{display:flex;align-items:center;gap:6px;font-size:12px;color:#333;text-decoration:none;white-space:nowrap;flex:none}
.more-link svg{width:19px;height:19px}
p.copy{font-size:12px;line-height:18px;text-align:justify;color:var(--text)}
.about-photo{position:absolute;left:0;top:58px;width:140px;height:160px;border:1px solid #d6d6d6;border-radius:3px;background:linear-gradient(#f4f2ee,#e6e3dc)}
.about-text{position:absolute;left:160px;top:59px;width:300px}
.about-text p+p{margin-top:18px}
.features-intro{margin-top:22px}
.feature-row{display:flex;justify-content:space-between;margin-top:15px}
.feature{width:140px;height:109px;border:1px solid var(--card-border);border-radius:3px;background:radial-gradient(ellipse at center,#fff 55%,#f1ede8);display:flex;flex-direction:column;align-items:center;padding-top:24px;gap:10px;font-size:12px;font-weight:700;color:#555}
.feature svg{width:34px;height:34px}
.testimonials{display:flex;gap:20px;margin-top:24px}
.testimonial{width:220px}
.testimonial h3{font-size:14px;font-weight:700;color:#4a4f5e;margin-bottom:14px}
.news-box{margin-top:15px;border:1px solid var(--card-border);border-radius:3px;background:radial-gradient(ellipse at center,#fff 70%,#f3efea);padding:15px 18px 16px 14px}
.news-item{display:flex;align-items:center;gap:10px;font-size:14px;font-weight:700;color:#3f4450}
.news-item svg{width:17px;height:17px;flex:none}
.news-body{margin:8px 0 20px 26px}
.news-item+.news-item{margin-top:13px}
footer{position:absolute;left:0;top:661px;width:1200px;height:271px;border-top:2px solid #222;background:radial-gradient(ellipse 420px 160px at 300px 40px,var(--footer-glow),transparent),radial-gradient(ellipse 380px 150px at 860px 40px,#22392a,transparent),var(--footer-dark)}
.foot-title{position:absolute;top:22px;font-size:18px;font-weight:400;color:var(--footer-head);text-shadow:0 1px 1px #000}
.menu{position:absolute;left:127px;top:66px;width:141px;list-style:none}
.menu li{font-size:12px;font-weight:700;color:#e6e6e0;height:26px;line-height:18px;border-bottom:1px solid var(--footer-rule);box-shadow:0 1px 0 rgba(255,255,255,.06)}
.menu li::before{content:"•";color:#888;margin-right:5px}
.menu li:last-child{border:0;box-shadow:none;margin-top:4px}
.thumbs{position:absolute;left:367px;top:68px;display:flex;gap:21px}
.thumb{width:59px;height:71px;border:2px solid #3b4150;border-radius:3px;background:#fff;box-shadow:inset 0 0 0 1px #000}
.gallery-rule{position:absolute;left:367px;top:154px;width:300px;border-top:1px solid #000;box-shadow:0 1px 0 rgba(255,255,255,.07)}
.browse{position:absolute;left:566px;top:167px;display:flex;align-items:center;gap:6px;font-size:12px;color:#9a9a92;text-decoration:underline}
.contact{position:absolute;left:767px;top:68px;list-style:none;width:240px}
.contact li{display:flex;gap:8px;font-size:12px;line-height:18px;color:var(--footer-text);margin-bottom:14px}
.contact svg{width:17px;height:17px;flex:none;margin-top:1px}
</style>
</head>
<body>
<div class="top-fade"></div>

<section class="block" style="left:127px;top:58px">
  <div class="block-head"><h2 class="block-title">A few words about us</h2>
    <a class="more-link" href="#">More details <svg viewBox="0 0 19 19"><rect width="19" height="19" rx="3" fill="var(--arrow)"/><path d="M8 5l4.5 4.5L8 14" stroke="#fff" stroke-width="2.2" fill="none"/></svg></a></div>
  <div class="about-photo" role="img" aria-label="Photo of the holiday house"></div>
  <div class="about-text">
    <p class="copy">Lorem ipsum dolor sit amet, consectetuer adipiscing elit. Aenean commodo ligula eget dolor. Aenean massa. Cum sociis natoque penatibus et magnis dis parturient montes, nascetur ridiculus mus.</p>
    <p class="copy">Donec quam felis, ultricies nec, pellentesque eu, pretium quis, sem. Nulla consequat massa quis enim. Donec pede justo, fringilla vel, aliquet nec, vulputate eget, arcu. In enim justo, rhoncus ut, imperdiet a, venenatis vitae, justo.</p>
  </div>
</section>

<section class="block" style="left:607px;top:58px">
  <div class="block-head"><h2 class="block-title">How is Sorvimaja puhkemaja different?</h2>
    <a class="more-link" href="#">View all features <svg viewBox="0 0 19 19"><rect width="19" height="19" rx="3" fill="var(--arrow)"/><path d="M8 5l4.5 4.5L8 14" stroke="#fff" stroke-width="2.2" fill="none"/></svg></a></div>
  <p class="copy features-intro">Lorem ipsum dolor sit amet, consectetuer adipiscing elit. Aenean commodo ligula eget dolor. Aenean massa. Cum sociis natoque penatibus et magnis dis parturient montes, nascetur ridiculus mus.</p>
  <div class="feature-row">
    <div class="feature"><svg viewBox="0 0 34 34" fill="none" stroke="#4b4f5c" stroke-width="2.5"><path d="M11 18a9 9 0 1 1 12 0c-1.5 1.5-2 3-2 5h-8c0-2-.5-3.5-2-5z"/><path d="M13 27h8M14 31h6"/></svg>Lorem ipsum</div>
    <div class="feature"><svg viewBox="0 0 34 34" fill="none" stroke="#4b4f5c" stroke-width="2.5"><path d="M6 12a13 13 0 1 1-1 8"/><path d="M17 9v8h6"/><path d="M3 10l3 3 3-3"/><text x="4" y="30" font-size="12" font-family="Arimo,sans-serif" font-weight="700" fill="#4b4f5c" stroke="none">$</text></svg>Donec quam felis</div>
    <div class="feature"><svg viewBox="0 0 34 34"><path d="M11 15v-4a6 6 0 0 1 12 0v4" fill="none" stroke="#4b4f5c" stroke-width="3"/><rect x="7" y="15" width="20" height="16" rx="2" fill="#4b4f5c"/><rect x="15.5" y="20" width="3" height="6" fill="#fff"/></svg>Cum sociis natoque</div>
  </div>
</section>

<section class="block" style="left:127px;top:368px">
  <div class="block-head"><h2 class="block-title">What our clients say</h2>
    <a class="more-link" href="#">Read all testimonials <svg viewBox="0 0 19 19"><rect width="19" height="19" rx="3" fill="var(--arrow)"/><path d="M8 5l4.5 4.5L8 14" stroke="#fff" stroke-width="2.2" fill="none"/></svg></a></div>
  <div class="testimonials">
    <div class="testimonial"><h3>John Doe - Lorem Ipsum</h3><p class="copy">Lorem ipsum dolor sit amet sit et, consectetuer adipiscing elit. Aenean commodo ligula eget dolor. Aenean massa. Cum sociis natoque penatibus et magnis dis parturient montes, nasc etur ridiculus mus.</p></div>
    <div class="testimonial"><h3>Dolores Sit - Aenean massa</h3><p class="copy">Lorem ipsum dolor sit amet sit et, consectetuer adipiscing elit. Aenean commodo ligula eget dolor. Aenean massa. Cum sociis natoque penatibus et magnis dis parturient montes, nasc etur ridiculus mus.</p></div>
  </div>
</section>

<section class="block" style="left:607px;top:368px">
  <div class="block-head"><h2 class="block-title">News</h2>
    <a class="more-link" href="#">View all news <svg viewBox="0 0 19 19"><rect width="19" height="19" rx="3" fill="var(--arrow)"/><path d="M8 5l4.5 4.5L8 14" stroke="#fff" stroke-width="2.2" fill="none"/></svg></a></div>
  <div class="news-box">
    <div class="news-item"><svg viewBox="0 0 17 17"><circle cx="8.5" cy="8.5" r="8.5" fill="var(--arrow)"/><path d="M5 8.5h7" stroke="#fff" stroke-width="2"/></svg>Lorem ipsum dolor</div>
    <p class="copy news-body">Lorem ipsum dolor sit amet sit et, consectetuer adipiscing elit. Aenean commodo ligula eget dolor. Aenean massa. Cum sociis natoque pena tibus et magnis dis parturient montes, nasc etur ridiculus mus.</p>
    <div class="news-item"><svg viewBox="0 0 17 17"><circle cx="8.5" cy="8.5" r="8.5" fill="var(--arrow)"/><path d="M5 8.5h7M8.5 5v7" stroke="#fff" stroke-width="2"/></svg>Aenean commodo ligula eget dolor</div>
    <div class="news-item"><svg viewBox="0 0 17 17"><circle cx="8.5" cy="8.5" r="8.5" fill="var(--arrow)"/><path d="M5 8.5h7M8.5 5v7" stroke="#fff" stroke-width="2"/></svg>Cum sociis natoque penatibus</div>
  </div>
</section>

<footer>
  <h2 class="foot-title" style="left:127px">Main menu</h2>
  <ul class="menu"><li>Tutvustus</li><li>Hinnakiri</li><li>Asukoht</li><li>Galerii</li><li>Huvitavat</li><li>Kontakt</li></ul>

  <h2 class="foot-title" style="left:367px">Gallery</h2>
  <div class="thumbs">
    <div class="thumb" role="img" aria-label="Gallery photo of the house"></div>
    <div class="thumb" role="img" aria-label="Gallery photo of the sea shore"></div>
    <div class="thumb" role="img" aria-label="Gallery photo of the garden"></div>
    <div class="thumb" role="img" aria-label="Gallery photo of the interior"></div>
  </div>
  <div class="gallery-rule"></div>
  <div class="browse">Browse gallery <svg width="14" height="14" viewBox="0 0 14 14" fill="none" stroke="#9a9a92" stroke-width="1.5"><circle cx="7" cy="7" r="6"/><path d="M6 4l3 3-3 3"/></svg></div>

  <h2 class="foot-title" style="left:767px">Contact information</h2>
  <ul class="contact">
    <li><svg viewBox="0 0 17 17"><path d="M1 8l7.5-6L16 8h-2v7H3V8z" fill="#c9bfa8"/><rect x="7" y="10" width="3" height="5" fill="#0f1812"/></svg>Sorvi talu, Rannaküla, Meremaa vald, Harjumaa 74010</li>
    <li><svg viewBox="0 0 17 17"><rect x="2" y="4" width="13" height="9" fill="#c9bfa8"/><path d="M2 4l6.5 5L15 4" stroke="#0f1812" fill="none"/></svg>info@sorvimaja.ee</li>
    <li><svg viewBox="0 0 17 17"><path d="M1 3h10v6H5l-3 3V9H1z" fill="#c9bfa8"/><path d="M12 6h4v6h-1v3l-3-3H7v-2h5z" fill="#c9bfa8"/></svg>+372 55 01 234</li>
  </ul>
</footer>
</body>
</html>
```